New Header Grpahic and Banner Ads for SEO Company

Harbor Net Mentor is an Online Advertising Company specializing in SEO, Social Media Marketing, Chatterbook Marketing, Quipster Marketing, Mobile Websites, E-Commerce and much more.

Header Graphic:
We need a new header graphic because we are updating our website with a new look and feel.

Must be 949 pixels wide and on a black background. We currently don't like our current header graphic because it uses a stock photo that a lot of other companies use, and doesn't feel authentic.

It might be a good idea to use the 2 photos on our website from the About Us page, but this is not a hard requirement. It may be better to do something completely different. Use your best judgment.

Banner Ads:

We need a package of 4 banner ads that we can use to advertise on other websites. Although we specialize in SEO, we are hoping to get banner ads that tell the user that we do not only SEO, but many other services as well.
It would be good if the text within these banners moved, or if they had some element of movement to be eye catching like as an animated GIF. - This would be nice, but is not a hard requirement.

The sizes of the banners that we need are:
125x125
300x250
470x60
728x90

It would be ideal to see designs for banners that advertise our company in general, and maybe some that match our products found at:

http://www.harbornetmentor-example.com/seo
http://www.harbornetmentor-example.com/social-media-marketing/social-media-optimization

-If we could customize the text within the banners ourselves later, that would also help. For example if we launch a new product or service, it would be great not to have to design a graphic from scratch. Perhaps putting text on a special layer inside photoshop could accomplish this.

Industry/Entity Type

It Company

```html
<!DOCTYPE html>
<html lang="en">
<head>
<meta charset="utf-8">
<title>Harbor Net Mentor – Banner Ads</title>
<link rel="stylesheet" href="https://fonts.googleapis.com/css2?family=Open+Sans:wght@600;700&display=swap">
<style>
  :root {
    --canvas-bg: #000000;
    --banner-light: #ffffff;
    --banner-shade: #e4e5e7;
    --brand-red: #c21f32;
    --button-top: #fff27a;
    --button-mid: #ffd63a;
    --button-bottom: #f5a800;
    --button-text: #3a3a3a;
    --logo-text: #3b3b3b;
    --photo-dark: #1e1e22;
    --photo-mid: #55565c;
  }
  * { box-sizing: border-box; margin: 0; padding: 0; }
  html, body {
    width: 1200px;
    height: 900px;
    overflow: hidden;
    background: var(--canvas-bg);
  }
  .ad-sheet {
    position: relative;
    width: 1200px;
    height: 900px;
    font-family: "Open Sans", Arial, sans-serif;
  }
  .banner {
    position: absolute;
    width: 333px;
    height: 277px;
    overflow: hidden;
    background: linear-gradient(100deg, var(--banner-light) 0%, var(--banner-light) 35%, var(--banner-shade) 100%);
  }
  .col-1 { left: 68px; }
  .col-2 { left: 431px; }
  .col-3 { left: 794px; }
  .row-1 { top: 142px; }
  .row-2 { top: 451px; }

  .headline {
    position: absolute;
    left: 35px;
    top: 26px;
    height: 100px;
    width: 290px;
    display: flex;
    flex-direction: column;
    justify-content: center;
    color: var(--brand-red);
    font-weight: 600;
    font-size: 40px;
    line-height: 44px;
    letter-spacing: -0.4px;
    white-space: nowrap;
  }
  .headline--hero {
    top: 18px;
    font-weight: 700;
    font-size: 98px;
    line-height: 1;
    letter-spacing: -2px;
  }

  .team-photo {
    position: absolute;
    left: 172px;
    top: 140px;
    width: 161px;
    height: 137px;
    border-radius: 30px 30px 0 0;
    background: linear-gradient(180deg, var(--photo-mid) 0%, var(--photo-dark) 55%, var(--photo-dark) 100%);
  }

  .learn-more {
    position: absolute;
    left: 21px;
    top: 145px;
    width: 144px;
    height: 29px;
    border-radius: 15px;
    background: linear-gradient(180deg, var(--button-top) 0%, var(--button-mid) 50%, var(--button-bottom) 100%);
    box-shadow: 0 1px 2px rgba(0,0,0,0.25);
    color: var(--button-text);
    font-size: 16px;
    font-weight: 600;
    line-height: 29px;
    text-align: center;
  }

  .brand-mark {
    position: absolute;
    left: 23px;
    top: 200px;
    display: flex;
    align-items: center;
    gap: 6px;
  }
  .brand-dot {
    width: 34px;
    height: 34px;
    border-radius: 50%;
    background: var(--brand-red);
    flex: none;
  }
  .brand-name {
    color: var(--logo-text);
    font-size: 16px;
    font-weight: 600;
    line-height: 1.05;
    text-transform: uppercase;
    width: 105px;
  }

  .footer-band {
    position: absolute;
    left: 0;
    bottom: 0;
    width: 172px;
    height: 21px;
    background: var(--brand-red);
  }
</style>
</head>
<body>
<main class="ad-sheet">

  <section class="banner col-1 row-1">
    <h2 class="headline headline--hero">SEO</h2>
    <div class="team-photo" role="img" aria-label="Photo of three business people in dark suits, arms crossed"></div>
    <div class="learn-more">Learn More</div>
    <div class="brand-mark"><span class="brand-dot"></span><span class="brand-name">Harbor Net Mentor</span></div>
    <div class="footer-band"></div>
  </section>

  <section class="banner col-2 row-1">
    <h2 class="headline"><span>Social Media</span><span>Marketing</span></h2>
    <div class="team-photo" role="img" aria-label="Photo of three business people in dark suits, arms crossed"></div>
    <div class="learn-more">Learn More</div>
    <div class="brand-mark"><span class="brand-dot"></span><span class="brand-name">Harbor Net Mentor</span></div>
    <div class="footer-band"></div>
  </section>

  <section class="banner col-3 row-1">
    <h2 class="headline"><span>Chatterbook</span><span>Marketing</span></h2>
    <div class="team-photo" role="img" aria-label="Photo of three business people in dark suits, arms crossed"></div>
    <div class="learn-more">Learn More</div>
    <div class="brand-mark"><span class="brand-dot"></span><span class="brand-name">Harbor Net Mentor</span></div>
    <div class="footer-band"></div>
  </section>

  <section class="banner col-1 row-2">
    <h2 class="headline"><span>Quipster</span><span>Marketing</span></h2>
    <div class="team-photo" role="img" aria-label="Photo of three business people in dark suits, arms crossed"></div>
    <div class="learn-more">Learn More</div>
    <div class="brand-mark"><span class="brand-dot"></span><span class="brand-name">Harbor Net Mentor</span></div>
    <div class="footer-band"></div>
  </section>

  <section class="banner col-2 row-2">
    <h2 class="headline"><span>Mobile</span><span>Websites</span></h2>
    <div class="team-photo" role="img" aria-label="Photo of three business people in dark suits, arms crossed"></div>
    <div class="learn-more">Learn More</div>
    <div class="brand-mark"><span class="brand-dot"></span><span class="brand-name">Harbor Net Mentor</span></div>
    <div class="footer-band"></div>
  </section>

  <section class="banner col-3 row-2">
    <h2 class="headline"><span>E-Commerce</span></h2>
    <div class="team-photo" role="img" aria-label="Photo of three business people in dark suits, arms crossed"></div>
    <div class="learn-more">Learn More</div>
    <div class="brand-mark"><span class="brand-dot"></span><span class="brand-name">Harbor Net Mentor</span></div>
    <div class="footer-band"></div>
  </section>

</main>
</body>
</html>
```